Radiology Department needs a series of 3 facebook posts - similar design

We need a series of 3 posts for our facebook page, each one presenting the activity of one of 3 physicians.
The main design elements can be the same, the only thing that will change between posts will be the field of activity and name of the physician and the representative image of its activity.
If needed the design elements can be slightly different between posts for better adjustment to the representative images.
You can find as an attachment:
- Manual of institutional identity of the Hospital (Velmor Clinica)
- Our facebook cover page
- Our department video
- The representative images for each post, identified with the name of each physician
- The Institutional identity manual with the logo of "Brisa Medical School" - just for Dr Tomas Brandilo post.
So, each one of the three posts should state the name and field of activity of each physician, including somehow the corresponding representative image, and should have background innovative design elements.
Post 1:
Name of the physician: Prof. Doutor Rui Castelvo
Field of activity: Imagiologia Reumatológica e do Sistema Músculo-Esquelético
Image as an attachment
Post 2:
Name of the physician: Prof.ª Doutora Inês Barroca
Field of activity: Imagiologia Cardíaca
Image as an attachment
Post 3:
Name of the physician: Dr. Tomas Lupo
Field of activity: Tese de Doutoramento em Curso - Identificação da Lesão Cartilagínea Precoce. Com orientação do Prof. Doutor Rui Castelvo e Prof.ª Doutora Inês Sofia Carvalhal.
Image as an attachment
Just for Dr Tomas Lupo, the logo of Brisa Medical School should also be included (please check the corresponding institutional identity manual that was just added in documents).
Updates

Just for Dr Tomas Brandilo, the logo of Brisa Medical School should also be included (please check the corresponding institutional identity manual that was just added in documents).

Please note that we are just looking for 3 facebook POSTS, not facebook cover page, thanks.

Please kindly note that we are looking for facebook POST and NOT facebook cover page.

Target Market(s)

General Population

Industry/Entity Type

Health

Font styles to use
Other font styles liked:
• Check manual of institutional identity and try to approach if appropriate

Requirements
Must have
• Check project description.
Nice to have
• If the designer finds appropriate, the logo of the Hospital would be nice in all the three posts, the most simple one just stating "VelmorClinica" - please check the attached manual of institutional identity

```html
<!DOCTYPE html>
<html lang="pt">
<head>
<meta charset="utf-8">
<title>Velmor Clinica – Facebook Posts</title>
<link rel="stylesheet" href="https://fonts.googleapis.com/css2?family=Oswald:wght@500&family=Work+Sans:wght@300;400;600;700&display=swap">
<style>
  :root {
    --sheet-bg: #1ba3bf;
    --card-bg: #02171c;
    --card-band: #0a262d;
    --accent: #fbb41c;
    --brand: #1d5f72;
    --brand-circle: #14748a;
    --text: #ffffff;
  }
  * { margin: 0; padding: 0; box-sizing: border-box; }
  html, body { width: 1200px; height: 2648px; overflow: hidden; }
  body {
    background: var(--sheet-bg);
    font-family: "Work Sans", Arial, sans-serif;
    color: var(--text);
    position: relative;
  }
  .sheet-title {
    position: absolute; top: 82px; left: 0; width: 1200px;
    text-align: center;
    font-family: "Oswald", "Arial Narrow", sans-serif;
    font-weight: 500; font-size: 36px; letter-spacing: 1px;
  }
  .sheet-size {
    position: absolute; top: 140px; left: 0; width: 1200px;
    text-align: center; font-weight: 300; font-size: 32px;
  }
  .post {
    position: absolute; left: 89px; width: 1022px; height: 536px;
    background:
      linear-gradient(110deg, transparent 0 23%, rgba(255,255,255,0.035) 23% 30%, transparent 30% 82%, rgba(255,255,255,0.025) 82% 90%, transparent 90%),
      radial-gradient(ellipse at 15% 0%, var(--card-band), transparent 55%),
      var(--card-bg);
    box-shadow: 0 18px 40px rgba(0,0,0,0.35);
    overflow: hidden;
  }
  .post--1 { top: 241px; }
  .post--2 { top: 833px; }
  .post--3 { top: 1424px; }
  .post--4 { top: 2016px; }
  .post__image {
    position: absolute; left: 55px; top: 82px; width: 385px; height: 384px;
    border: 10px solid var(--accent);
  }
  .image-hand { background: radial-gradient(ellipse at 50% 45%, #8c8c8c 0%, #3c3c3c 45%, #050505 80%); }
  .image-heart { background: radial-gradient(ellipse at 45% 55%, #7a241a 0%, #4a120c 35%, #000 70%); }
  .image-knee { background: radial-gradient(ellipse at 50% 50%, #1a2fa8 0%, #1f3ed8 45%, #0b1a6e 90%); }
  .brand {
    position: absolute; left: 491px; top: 72px;
    display: flex; align-items: center; gap: 10px;
  }
  .brand__circle {
    width: 69px; height: 69px; border-radius: 50%;
    background: var(--brand-circle);
  }
  .brand__name {
    font-weight: 600; font-size: 42px; color: var(--brand);
  }
  .brand__tagline {
    position: absolute; left: 566px; top: 143px;
    font-weight: 400; font-size: 16px; color: var(--brand);
  }
  .physician__name {
    position: absolute; left: 489px; top: 199px;
    font-weight: 700; font-size: 26px; letter-spacing: 1.2px;
  }
  .physician__field {
    position: absolute; left: 489px; top: 237px; width: 480px;
    font-weight: 300; font-size: 27px; line-height: 35px; letter-spacing: 0.5px;
  }
  .physician__field--long {
    font-weight: 400; font-size: 17.5px; line-height: 22px; letter-spacing: -0.2px; width: 480px;
  }
  .post__arc { position: absolute; left: 455px; bottom: 0; width: 510px; height: 28px; }
  .partner {
    position: absolute; right: 582px; top: 484px;
    font-weight: 700; font-size: 20px; letter-spacing: 0.3px; color: var(--text);
    white-space: nowrap;
  }
</style>
</head>
<body>
  <h1 class="sheet-title">3 IMAGE POSTS FOR VELMOR CLINICA FACEBOOK PAGE</h1>
  <p class="sheet-size">SIZE:1200 × 630 PX</p>

  <section class="post post--1">
    <div class="post__image image-hand" role="img" aria-label="Angiografia das mãos em tons de cinzento"></div>
    <div class="brand"><span class="brand__circle"></span><span class="brand__name">VelmorClinica</span></div>
    <p class="brand__tagline">Cuidamos de si com proximidade</p>
    <h2 class="physician__name">PROF. DOUTOR RUI CASTELVO</h2>
    <p class="physician__field">Imagiologia Reumatológica e do Sistema Músculo-Esquelético</p>
    <svg class="post__arc" viewBox="0 0 510 28" preserveAspectRatio="none"><path d="M0 28 Q255 -20 510 28 Z" fill="var(--accent)"/></svg>
  </section>

  <section class="post post--2">
    <div class="post__image image-heart" role="img" aria-label="Reconstrução 3D do coração com artérias coronárias"></div>
    <div class="brand"><span class="brand__circle"></span><span class="brand__name">VelmorClinica</span></div>
    <p class="brand__tagline">Cuidamos de si com proximidade</p>
    <h2 class="physician__name">PROF.ª DOUTORA INÊS BARROCA</h2>
    <p class="physician__field">Imagiologia Cardíaca</p>
    <svg class="post__arc" viewBox="0 0 510 28" preserveAspectRatio="none"><path d="M0 28 Q255 -20 510 28 Z" fill="var(--accent)"/></svg>
  </section>

  <section class="post post--3">
    <div class="post__image image-knee" role="img" aria-label="Mapa de ressonância magnética do joelho em tons de azul"></div>
    <p class="partner">BRISA MEDICAL SCHOOL</p>
    <div class="brand"><span class="brand__circle"></span><span class="brand__name">VelmorClinica</span></div>
    <p class="brand__tagline">Cuidamos de si com proximidade</p>
    <h2 class="physician__name">DR. TOMAS LUPO</h2>
    <p class="physician__field physician__field--long">Tese de Doutoramento em Curso - Identificação da Lesão Cartilagínea Precoce. Com orientação do Prof. Doutor Rui Castelvo e Prof.ª Doutora Inês Sofia Carvalhal.</p>
    <svg class="post__arc" viewBox="0 0 510 28" preserveAspectRatio="none"><path d="M0 28 Q255 -20 510 28 Z" fill="var(--accent)"/></svg>
  </section>

  <section class="post post--4">
    <div class="post__image image-knee" role="img" aria-label="Mapa de ressonância magnética do joelho em tons de azul"></div>
    <div class="brand"><span class="brand__circle"></span><span class="brand__name">VelmorClinica</span></div>
    <p class="brand__tagline">Cuidamos de si com proximidade</p>
    <h2 class="physician__name">DR. TOMAS LUPO</h2>
    <p class="physician__field physician__field--long">Tese de Doutoramento em Curso - Identificação da Lesão Cartilagínea Precoce. Com orientação do Prof. Doutor Rui Castelvo e Prof.ª Doutora Inês Sofia Carvalhal.</p>
    <svg class="post__arc" viewBox="0 0 510 28" preserveAspectRatio="none"><path d="M0 28 Q255 -20 510 28 Z" fill="var(--accent)"/></svg>
  </section>
</body>
</html>
```